Corporate flyer highlighting service offering for PR agency

A corporate flyer is needed for a new service offering that we are doing. The product name is HarborLeap it is a marketing and communications services offering for companies who are getting ready to sell their business. If we are really happy with the designer's work, there will be a great deal more projects. I am looking for a clean design with a few pops of color from my site. https://quillmarsh.partners. I am looking for a good design with data in sections. I am looking for a clean design that feels high-end but not cluttered. Please do not use images of people. Please see the following examples of types of designs I like.
https://www.tackboard.example/pin/839201746530918264/
https://www.tackboard.example/pin/402918375561029847/
https://assets.stockvale.example/corporate-flyer-template-KRTPMB
https://designbrook.example/item/corporate-flyer-template/81046395?s_rank=8
https://assets.stockvale.example/corporate-business-flyer-template-93PX7D

I had to place the project on hold as I choose the wrong type of project and did not get many designs as a result. I am reposting this with an updated brief.

Target Market(s)

Business sellers and brokers

Industry/Entity Type

Marketing for business sellers

Font styles to use
Sans Serif

Requirements
Must have
• Good quality design with content in sections. Clean and high end feeling is a must.
Should not have
• A lot of images of people.

```html
<!DOCTYPE html>
<html lang="en">
<head>
<meta charset="utf-8">
<title>HarborLeap – Quillmarsh Partners</title>
<link rel="stylesheet" href="https://fonts.googleapis.com/css2?family=Montserrat:wght@400;500;600;700&family=Oswald:wght@400;500&display=swap">
<style>
:root{
  --orange:#f15a24;
  --amber:#f7941d;
  --red:#e8412c;
  --blue:#1c8ad6;
  --navy:#1f3a6e;
  --green:#7ac143;
  --ink:#2b2b2b;
  --text:#444;
  --grey:#e6e6e6;
  --page-bg:#ffffff;
}
*{box-sizing:border-box;margin:0;padding:0}
html,body{width:1200px;height:4000px;overflow:hidden;background:#fff;font-family:'Montserrat',sans-serif;color:var(--text)}
.page{position:absolute;left:156px;width:888px;height:1153px;background:var(--page-bg);box-shadow:0 6px 14px rgba(0,0,0,.28);overflow:hidden}
.page-1{top:125px}.page-2{top:1416px}.page-3{top:2703px}
.abs{position:absolute}
.copy{font-size:10.5px;line-height:14.5px;color:var(--text)}
.label{position:absolute;display:inline-block;padding:2px 6px;font-size:17px;font-weight:600;letter-spacing:.5px;color:#fff;line-height:20px}
.label-green{background:var(--green)}.label-blue{background:var(--blue)}.label-orange{background:var(--amber)}
.ticks{list-style:none}
.ticks li{position:relative;padding-left:18px;margin-bottom:6px}
.ticks li::before{content:"";position:absolute;left:0;top:2px;width:10px;height:10px;border-radius:50%;background:var(--red)}
.ticks li::after{content:"";position:absolute;left:3px;top:4px;width:4px;height:2.5px;border-left:1.5px solid #fff;border-bottom:1.5px solid #fff;transform:rotate(-45deg)}
.caps{text-transform:uppercase;font-weight:600;color:var(--ink);letter-spacing:.4px}

/* page 1 */
.brand{left:36px;top:40px;width:330px;text-align:center;color:var(--navy);font-weight:600}
.brand-mark{width:46px;height:46px;background:var(--blue);margin:0 auto 18px}
.brand-name{font-size:31px;letter-spacing:1px;line-height:34px}
.brand-sub{font-size:14px;letter-spacing:5px;margin-top:2px}
.headline{left:36px;top:218px;font-family:'Oswald',sans-serif;line-height:1;width:420px}
.headline .h-a{font-size:44px;color:var(--orange)}
.headline .h-b{font-size:31px;color:var(--blue);margin-top:3px}
.headline .h-c{font-size:41px;color:var(--green)}
.headline .h-d{font-size:18px;color:var(--blue);margin-top:3px}
.quote-box{color:#fff;font-size:10.5px;line-height:14px;padding:48px 24px 0}
.quote-mark{position:absolute;left:50%;top:-12px;margin-left:-24px;width:48px;height:38px}
.help-box{background:var(--grey);padding:38px 24px 0}

.foot{left:36px;top:1090px;width:816px;height:28px;font-size:11px;font-weight:600;color:var(--ink);display:flex;align-items:center}
.foot span{display:flex;align-items:center;gap:8px}
.foot svg{flex:none}
.badge{width:18px;height:18px;border-radius:50%;background:#333;display:inline-block}
.badge-sq{width:22px;height:24px;border:1.5px solid #333;display:inline-block}

/* page 2 & 3 */
.sec-title{position:absolute;display:flex;align-items:center;gap:10px;font-size:20px;font-weight:600;color:var(--blue);letter-spacing:.3px}
.sec-icon{width:28px;height:28px;border-radius:50%;background:var(--green);border:3px solid #d9efc6;position:relative;flex:none}
.sec-icon::after{content:"";position:absolute;left:6px;top:7px;width:10px;height:8px;border:2px solid #fff;border-radius:2px}
.brand-row{position:absolute;left:39px;width:810px}
.brand-row .item{position:absolute;left:0;width:200px;font-size:15px;line-height:18px;padding-left:26px}
.brand-row .item::before{content:"";position:absolute;left:0;top:3px;width:11px;height:11px;border-radius:50%;background:var(--red)}
.brand-row .desc{position:absolute;left:231px;width:580px}
.hexes{left:600px;top:515px;width:260px;height:140px}
.boxed{position:absolute;left:39px;width:810px;padding:3px 8px;font-size:10px;line-height:13.5px;border:1.5px solid}
</style>
</head>
<body>

<!-- PAGE ONE -->
<section class="page page-1">
  <svg class="abs" style="left:0;top:0" width="888" height="470" viewBox="0 0 888 470">
    <polygon points="796,392 888,330 888,458" fill="var(--green)"/>
    <polygon points="462,0 888,0 888,330 796,392 498,392" fill="var(--blue)"/>
    <defs><linearGradient id="bld" x1="0" y1="0" x2="1" y2="1"><stop offset="0" stop-color="#f3c98a"/><stop offset=".5" stop-color="#8a7a6a"/><stop offset="1" stop-color="#4a4d52"/></linearGradient></defs>
    <polygon role="img" aria-label="Photo of a modern glass office building at sunset" points="470,0 888,0 888,318 790,382 505,382" fill="url(#bld)"/>
  </svg>

  <div class="abs brand">
    <div class="brand-mark"></div>
    <div class="brand-name">QUILLMARSH</div>
    <div class="brand-sub">PARTNERS</div>
  </div>

  <div class="abs headline">
    <div class="h-a">HARBORLEAP PROVIDES</div>
    <div class="h-b">EXECUTIVES &amp; BUSINESS OWNERS</div>
    <div class="h-c">WITH CLEAR GUIDANCE</div>
    <div class="h-d">TO UNLOCK NON-FINANCIAL VALUE AHEAD OF AN EXIT</div>
  </div>

  <div class="abs copy" style="left:39px;top:402px;width:755px">
    <p>A strong communication and marketing strategy can significantly increase the value of your business leading up to an exit. Buyers are looking to mitigate risk and unlock potential value as a catalyst for clear growth potential.</p>
    <p style="margin-top:9px">Highlighting your company's success in the marketplace, identifying, and mitigating reputation risks before buyers do, enhancing employee engagement, finding hidden opportunities to boost marketing KPIs and showcasing IP, data, and innovation, can make a significant difference in valuation.</p>
  </div>

  <span class="label label-green" style="left:39px;top:506px">ABOUT US</span>
  <p class="abs copy" style="left:39px;top:542px;width:380px">We design and implement communication and marketing strategies that deliver significant increases in brand awareness, identify reputational risks, and enhance brand perception, helping owners and investors to realize premium values for their companies. We support owners and companies through:</p>
  <div class="abs caps" style="left:39px;top:632px;font-size:11px;line-height:26px">
    <div style="display:flex;gap:22px">
      <ul class="ticks"><li>Company exit preparation</li></ul>
      <ul class="ticks"><li>M&amp;A</li></ul>
      <ul class="ticks"><li>IPO</li></ul>
    </div>
    <div style="display:flex;gap:22px">
      <ul class="ticks"><li>Spinoff/Divestiture</li></ul>
      <ul class="ticks"><li>New leadership/investor</li></ul>
    </div>
  </div>

  <div class="abs quote-box" style="left:477px;top:505px;width:372px;height:170px;background:var(--orange)">
    <svg class="quote-mark" viewBox="0 0 48 38"><polygon points="0,0 48,0 48,26 24,38 0,26" fill="var(--orange)"/><text x="24" y="30" text-anchor="middle" font-family="Montserrat,sans-serif" font-weight="700" font-size="30" fill="#fff">”</text></svg>
    <p>US institutional investors believe that Investor Relations (IR) accounts for a total variance of 30% in a company's valuation – from a premium of 10% for “superb” IR to a discount of 20% for “poor” IR.</p>
    <p style="margin-top:16px">---Lindcrest Research Group, “Harnessing IR's Power to Impact a Company's Valuation.”</p>
  </div>

  <p class="abs copy" style="left:39px;top:691px;width:800px">Few sellers would list their home without first inspecting, repairing broken items, and making updates to highlight the positive aspects --increasing appeal to buyers. However, countless business owners leave money on the table during corporate exits due to a lack of preparation.</p>

  <svg class="abs" style="left:850px;top:735px" width="24" height="24" viewBox="0 0 24 24"><polygon points="12,1 22,6.5 22,17.5 12,23 2,17.5 2,6.5" fill="var(--blue)"/></svg>

  <span class="label label-blue" style="left:39px;top:771px">OUR TEAM</span>
  <p class="abs copy" style="left:39px;top:802px;width:382px">Our team of executive-level communications and marketing experts brings deep buy and sell-side experience. We have played critical roles in the acquisition, integration, and disposition process. Our mix of financial services expertise combined with decades of experience leading internal and external communications, marketing and investor relations teams gives us a unique perspective on identifying and unlocking non-financial areas of value and mitigating non-financial risks before exit.</p>

  <div class="abs help-box copy" style="left:477px;top:773px;width:372px;height:165px">
    <p>While accounting and investment banking teams are hard at work increasing value from a financial perspective, we help organizations enhance their valuation by identifying areas that will appeal most to buyers and ensuring those elements of your business are visible and memorable to those who matter most.</p>
  </div>
  <span class="label label-orange" style="left:497px;top:763px">WE HELP</span>

  <h2 class="abs" style="left:39px;top:966px;font-size:18px;font-weight:600;color:var(--ink);letter-spacing:.3px">WE HELP COMPANIES INCREASE VALUATION BY:</h2>
  <ul class="abs ticks caps" style="left:39px;top:1004px;width:300px;font-size:11px;line-height:13px">
    <li style="margin-bottom:10px">Highlighting value in a clear and visible way</li>
    <li>Streamlining the exit process</li>
  </ul>
  <ul class="abs ticks caps" style="left:396px;top:1004px;width:460px;font-size:11px;line-height:13px">
    <li style="margin-bottom:8px">Identifying potential risks and suggesting mitigation measures</li>
    <li>Creating a polished presence in the market ahead of buyer interest</li>
  </ul>

  <div class="abs foot">
    <span style="width:262px"><svg width="18" height="18" viewBox="0 0 18 18"><circle cx="9" cy="9" r="7.5" fill="none" stroke="var(--blue)" stroke-width="1.6"/><ellipse cx="9" cy="9" rx="3.3" ry="7.5" fill="none" stroke="var(--blue)" stroke-width="1.3"/><line x1="1.5" y1="9" x2="16.5" y2="9" stroke="var(--blue)" stroke-width="1.3"/></svg>www.quillmarsh.partners</span>
    <span style="width:392px"><svg width="18" height="14" viewBox="0 0 18 14"><rect x="1" y="1" width="16" height="12" fill="var(--blue)"/><polyline points="1,1 9,8 17,1" fill="none" stroke="#fff" stroke-width="1.4"/></svg>info@quillmarsh.partners</span>
    <span style="width:90px"><svg width="14" height="18" viewBox="0 0 14 18"><path d="M7 17C3 11 1 8.5 1 6a6 6 0 0 1 12 0c0 2.5-2 5-6 11z" fill="var(--blue)"/><circle cx="7" cy="6" r="2.2" fill="#fff"/></svg>Riverton</span>
    <span style="gap:5px"><i class="badge"></i><i class="badge"></i><i class="badge-sq"></i></span>
  </div>
</section>

<!-- PAGE TWO -->
<section class="page page-2">
  <svg class="abs" style="left:620px;top:0" width="268" height="250" viewBox="0 0 268 250">
    <polygon points="0,0 268,0 268,160" fill="var(--green)"/>
    <polygon points="150,0 268,0 268,250" fill="var(--amber)"/>
    <polygon points="225,0 268,0 268,120" fill="var(--red)"/>
  </svg>

  <span class="label label-blue" style="left:39px;top:38px">PROVIDES</span>
  <p class="abs copy" style="left:39px;top:76px;width:660px">HarborLeap provides executives &amp; business owners with clear guidance to unlock value ahead of an exit. Our non-disruptive, ala-carte process enables us to work with sellers on specific areas or to do a complete analysis &amp; recommendation and can include:</p>

  <h2 class="abs" style="left:39px;top:155px;font-size:20px;line-height:24px;font-weight:600;color:var(--blue)">BRAND ANALYSIS<br>AND RECOMMENDATIONS</h2>
  <div class="abs" style="left:356px;top:156px;width:1px;height:44px;background:#bbb"></div>
  <p class="abs copy" style="left:372px;top:158px;width:460px">Strong brands command a higher valuation. We conduct a brand analysis, providing clear and detailed recommendations to enhance your value proposition and help you stand out from the crowd:</p>

  <div class="brand-row" style="top:224px">
    <div class="item caps">Current external position among competitors</div>
    <p class="desc copy">We look at how your brand measures up based on external competitive analysis, positioning in the media and analyst community, and across other digital channels.</p>
  </div>
  <div class="brand-row" style="top:296px">
    <div class="item caps">Physical brand image</div>
    <p class="desc copy">A little bit of paint and updated fixtures can go a long way when increasing the value of a home. The same is true for businesses. Our audit evaluates non-disruptive steps your company can take to enhance your brand look and feel before sale.</p>
  </div>
  <div class="brand-row" style="top:361px">
    <div class="item caps">Employee brand perception</div>
    <p class="desc copy">We conduct a high-level external audit with recommendations to enhance engagement for current and prospective employees.</p>
  </div>
  <div class="brand-row" style="top:416px">
    <div class="item caps">Customer brand perception</div>
    <p class="desc copy">We conduct a high-level external audit showcasing how customers perceive your brand in the market. We then provide recommendations for enhancing engagement and maximizing value.</p>
  </div>

  <svg class="abs" style="left:862px;top:428px" width="26" height="40" viewBox="0 0 26 40"><polygon points="13,2 24,8 24,20 13,26 2,20 2,8" fill="#e3f0d6"/></svg>

  <h2 class="abs" style="left:39px;top:480px;font-size:17px;font-weight:600;color:var(--green)">CUSTOMER RETENTION GUIDE STATISTICS &amp; PRESCRIPTION CUTTING COSTS</h2>
  <ul class="abs ticks copy" style="left:39px;top:518px;width:540px;font-size:9.5px;line-height:13px">
    <li style="margin-bottom:14px">A <b style="color:var(--blue);font-weight:500">5% increase</b> in customer retention correlates with at least a <b style="color:var(--blue);font-weight:500">25% increase</b> in profit, according to an analysis by Corwen and Company.<br><b style="color:var(--ink)">(https://media.corwen.example/Images/CC_Prescription_cutting_costs.pdf)</b></li>
    <li>It costs <b style="color:var(--blue);font-weight:500">5 times</b> more to acquire a new customer than to retain a current one and <b style="color:var(--blue);font-weight:500">16 times</b> more to get new customers to the same spending level as existing ones. <b style="color:var(--ink)">(https://marketpulse.example/customer-retention-guide-statistics/)</b></li>
  </ul>
  <svg class="abs hexes" viewBox="0 0 260 140" font-family="Montserrat,sans-serif" font-weight="700" text-anchor="middle" fill="#fff">
    <g><polygon points="30,3 60,20 60,54 30,71 0,54 0,20" fill="var(--green)" stroke="#fff" stroke-width="3"/><polygon points="30,3 60,20 60,54 30,71 0,54 0,20" fill="none" stroke="var(--green)" stroke-width="1.5" transform="translate(-3,-3) scale(1.1)"/><text x="30" y="43" font-size="16">5<tspan font-size="8" dy="-6">%</tspan></text></g>
    <g transform="translate(120,0)"><polygon points="30,3 60,20 60,54 30,71 0,54 0,20" fill="var(--amber)" stroke="#fff" stroke-width="3"/><polygon points="30,3 60,20 60,54 30,71 0,54 0,20" fill="none" stroke="var(--amber)" stroke-width="1.5" transform="translate(-3,-3) scale(1.1)"/><text x="30" y="36" font-size="16">5</text><text x="30" y="48" font-size="8">TIMES</text></g>
    <g transform="translate(60,62)"><polygon points="30,3 60,20 60,54 30,71 0,54 0,20" fill="var(--blue)" stroke="#fff" stroke-width="3"/><polygon points="30,3 60,20 60,54 30,71 0,54 0,20" fill="none" stroke="var(--blue)" stroke-width="1.5" transform="translate(-3,-3) scale(1.1)"/><text x="30" y="43" font-size="16">25<tspan font-size="8" dy="-6">%</tspan></text></g>
    <g transform="translate(180,62)"><polygon points="30,3 60,20 60,54 30,71 0,54 0,20" fill="var(--red)" stroke="#fff" stroke-width="3"/><polygon points="30,3 60,20 60,54 30,71 0,54 0,20" fill="none" stroke="var(--red)" stroke-width="1.5" transform="translate(-3,-3) scale(1.1)"/><text x="30" y="36" font-size="16">16</text><text x="30" y="48" font-size="8">TIMES</text></g>
  </svg>

  <div class="sec-title" style="left:39px;top:670px"><i class="sec-icon"></i>DIGITAL &amp; TRADITIONAL MARKETING ANALYSIS &amp; RECOMMENDATIONS</div>
  <p class="abs copy" style="left:39px;top:710px;width:810px;font-size:9.5px;line-height:13px"><b style="color:var(--ink)">How much money are you leaving on the table?</b> Our marketing audits help organizations identify areas of hidden value that can have significant impacts on revenue and valuation. We optimize current activities and uncover new strategies to increase the effectiveness of current marketing spend. Areas we evaluate include:</p>
  <ul class="abs ticks copy" style="left:39px;top:775px;width:330px;font-size:9.5px;line-height:12px">
    <li style="margin-bottom:9px">Website traffic and conversion</li>
    <li style="margin-bottom:9px">CRM process review to identify strategies and recommendations to increase conversion and reactive old-leads</li>
    <li>Email marketing strategy</li>
  </ul>
  <ul class="abs ticks copy" style="left:464px;top:775px;width:380px;font-size:9.5px;line-height:12px">
    <li style="margin-bottom:9px">Automations and drip marketing</li>
    <li style="margin-bottom:9px">Social media strategy /presence</li>
    <li style="margin-bottom:9px">Partnership marketing</li>
    <li>Paid media analysis/strategy suggestion</li>
  </ul>

  <div class="sec-title" style="left:39px;top:880px"><i class="sec-icon"></i>MESSAGING AND CONTENT STRATEGY REVIEW AND ANALYSIS</div>
  <p class="abs copy" style="left:39px;top:922px;width:810px">It's about your valuation. Full and fair valuation requires a clear, compelling investment case articulated consistently to the right audience at the right time. Messaging to maximize your value in an acquisition or an IPO is quite different from typical selling messages for prospects, customers, or 'features &amp; business benefits' for press and analysts.  We understand the issues and speak the right language to maximize perception of value with key decision makers.</p>
  <ul class="abs ticks copy" style="left:39px;top:1000px;width:340px;font-size:9.5px;line-height:12px">
    <li style="margin-bottom:16px">Review and recommendations of key messaging and value proposition</li>
    <li>Analysis and recommendations to highlight data, IP, and innovation</li>
  </ul>
  <ul class="abs ticks copy" style="left:464px;top:1000px;width:380px;font-size:9.5px;line-height:12px">
    <li style="margin-bottom:16px">Analysis and recommendations to position key executives likely to remain with the company as thought leaders to help build value</li>
    <li>Analysis and recommendations to build employee engagement and retention enhancing your most valuable asset--your team</li>
  </ul>
</section>

<!-- PAGE THREE -->
<section class="page page-3">
  <svg class="abs" style="left:800px;top:0" width="88" height="275" viewBox="0 0 88 275">
    <polygon points="60,0 88,0 88,275" fill="var(--amber)"/>
    <polygon points="88,0 88,170 40,0" fill="var(--green)" opacity=".9"/>
    <polygon points="88,0 88,80 72,0" fill="var(--red)"/>
  </svg>

  <div class="sec-title" style="left:39px;top:38px"><i class="sec-icon"></i>MEDIA AND ANALYST STRATEGY DEVELOPMENT</div>
  <p class="abs copy" style="left:39px;top:84px;width:720px;font-size:9.5px;line-height:13px">Positive articles and inclusion in analyst reports pack a powerful punch when preparing your business for sale. We work with clients to develop a media strategy that goes beyond brand awareness, leveraging media to build a digital history of third-party validation targeted to enhance appeal to prospective buyers while generating traffic and connections, to enhance overall value.</p>
  <ul class="abs ticks copy" style="left:39px;top:164px;width:360px;font-size:9.5px;line-height:12px">
    <li style="margin-bottom:17px">Positioning to media and analyst community creating third party market validation</li>
    <li>Key angle recommendations</li>
  </ul>
  <ul class="abs ticks copy" style="left:435px;top:164px;width:380px;font-size:9.5px;line-height:12px">
    <li style="margin-bottom:17px">Announcement timeline and strategy planning to maximize media value of news</li>
    <li style="margin-bottom:10px">What is newsworthy</li>
    <li>How to position that news for the most significant impact</li>
  </ul>

  <h2 class="abs" style="left:39px;top:270px;font-size:20px;font-weight:600;color:var(--ink);letter-spacing:.3px">“WHITE HAT/BLACK HAT REVIEW”</h2>
  <p class="abs copy" style="left:39px;top:308px;width:790px;font-size:9.5px;line-height:13px">We take a buyer's communications and marketing approach to analyzing the client company and provide a “punch list” of things a potential buyer is likely to ask/request in due diligence from a comms/culture/marketing/reputation standpoint to ensure that when potential buyers start screening for sellers and evaluating them, the client company has the upper hand.</p>

  <p class="abs" style="left:39px;top:393px;width:395px;font-size:15.5px;line-height:19.5px;font-weight:500;color:var(--green)">Once the analysis is complete, we deliver actionable intelligence and recommendations to help leaders identify and quickly unlock areas that will boost value and appeal to prospective buyers. Work products include:</p>

  <div class="abs quote-box" style="left:473px;top:388px;width:375px;height:120px;background:var(--blue);padding-top:52px">
    <svg class="quote-mark" viewBox="0 0 48 38"><polygon points="0,0 48,0 48,26 24,38 0,26" fill="var(--blue)"/><text x="24" y="30" text-anchor="middle" font-family="Montserrat,sans-serif" font-weight="700" font-size="30" fill="#fff">”</text></svg>
    <p>“Strategy without tactics is the slowest route to victory. Tactics without strategy is the noise before defeat.</p>
    <p style="margin-top:4px">“ - Aldric Venn &nbsp;&nbsp;&nbsp;&nbsp;&nbsp;&nbsp;&nbsp;<b style="font-size:15px">25<sup style="font-size:8px">%</sup></b>&nbsp;&nbsp;&nbsp;&nbsp;&nbsp;<b style="font-size:9px">TIMES</b></p>
  </div>

  <div class="sec-title" style="left:39px;top:513px"><i class="sec-icon"></i>GAP ASSESSMENT</div>
  <p class="abs copy" style="left:77px;top:550px;width:760px;font-size:9.5px;line-height:13px">We provide a comprehensive seller report providing analysis and actionable recommendations to increase your valuation while identifying and mitigating non-financial risks.</p>

  <div class="sec-title" style="left:39px;top:590px"><i class="sec-icon" style="background:var(--blue);border-color:#cfe4f5"></i>STRATEGIC ROADMAP</div>
  <p class="abs copy" style="left:77px;top:628px;width:760px;font-size:9.5px;line-height:13px">Clients are given an actionable tactical roadmap based on the recommendation provided. Organizations can choose to implement key areas or include this powerful guide as part of their presentation to prospective buyers to highlight latent potential. The roadmap provides actionable steps buyers can take upon close as they make their case for your business with their investment committees.</p>

  <svg class="abs" style="left:34px;top:695px" width="820" height="182" viewBox="0 0 820 182" role="img" aria-label="Honeycomb collage of city office buildings, glass facades and tree-lined plazas">
    <defs><linearGradient id="city" x1="0" y1="0" x2="1" y2="0"><stop offset="0" stop-color="#2f5f6e"/><stop offset=".45" stop-color="#6f8fa8"/><stop offset=".75" stop-color="#d7a6b0"/><stop offset="1" stop-color="#5f8a4a"/></linearGradient></defs>
    <rect width="820" height="182" fill="url(#city)"/>
  </svg>

  <p class="boxed" style="top:890px;border-color:var(--orange)">Once the strategy integration roadmap is complete, your team can implement it on your timeline, we can work with your team providing guidance and executive-level support, or we can fully execute deliverables with our robust capabilities and team.</p>
  <p class="boxed" style="top:930px;border-color:var(--amber)">Our value proposition, based on delivering outcomes rather than just outputs, means that you receive the benefit and capability of deeply experienced corporate communications leaders without adding headcount or the time to identify, recruit, onboard and retain a new team member.</p>
  <p class="boxed" style="top:986px;border-color:var(--green)">We help organizations enhance their valuation by identifying areas that will appeal most to buyers and ensuring those elements of your business are visible and memorable to those who matter most.</p>
  <p class="boxed" style="top:1026px;border-color:var(--blue)">HarborLeap helps sellers maximize valuation and unlock hidden potential ahead of an exit--ensuring money is not left on the table.</p>

  <div class="abs foot" style="top:1092px">
    <span style="width:262px"><svg width="18" height="18" viewBox="0 0 18 18"><circle cx="9" cy="9" r="7.5" fill="none" stroke="var(--blue)" stroke-width="1.6"/><ellipse cx="9" cy="9" rx="3.3" ry="7.5" fill="none" stroke="var(--blue)" stroke-width="1.3"/><line x1="1.5" y1="9" x2="16.5" y2="9" stroke="var(--blue)" stroke-width="1.3"/></svg>www.quillmarsh.partners</span>
    <span style="width:392px"><svg width="18" height="14" viewBox="0 0 18 14"><rect x="1" y="1" width="16" height="12" fill="var(--blue)"/><polyline points="1,1 9,8 17,1" fill="none" stroke="#fff" stroke-width="1.4"/></svg>info@quillmarsh.partners</span>
    <span style="width:90px"><svg width="14" height="18" viewBox="0 0 14 18"><path d="M7 17C3 11 1 8.5 1 6a6 6 0 0 1 12 0c0 2.5-2 5-6 11z" fill="var(--blue)"/><circle cx="7" cy="6" r="2.2" fill="#fff"/></svg>Riverton</span>
    <span style="gap:5px"><i class="badge"></i><i class="badge"></i><i class="badge-sq"></i></span>
  </div>
</section>

</body>
</html>
```